Brightwell Ledger needs a Business Card

Designers!
More often than not, people want a cheap business card and often argue "I only want 100, not 500" - Years ago I worked in print and always wanted a client to ask for something that challenged me and would be great for my portfolio.

Years have past, and I dont have the time to do it myself so I'd love to see what everyone can offer.

Reason: Hey Guys, The designs are looking good but i've extended it a few more days as I wont be near a laptop and i'm trying to provide everyone feedback - Sorry!

Target Market(s)

Key decision makers, Potential Clients, Networking events and opportunities.

Industry/Entity Type

Business

Requirements
Must have
• Typography is very important. The type of paper is important.
The print, the shape. The creativity.
I'm very inspired by the below link
http://www.pelvarno.com/blog/business-card-design/

Nice to have
• Stencelled cutouts. Embossing, nice typography.
I'd like the business card to be a conversation piece itself.

Attached is an image of business cards i've had in the past.
Additionally, some logos i've recently had designed by MakerFlock.

```html
<!DOCTYPE html>
<html lang="en">
<head>
<meta charset="utf-8">
<title>Brightwell Ledger — Business Card</title>
<link rel="stylesheet" href="https://fonts.googleapis.com/css2?family=Questrial&display=swap">
<style>
  :root {
    --backdrop: #24506e;
    --card-top: #4a566c;
    --card-bottom: #36425a;
    --ink-white: #f2f4f7;
    --ink-soft: #c9d0db;
    --accent-green: #6ee02a;
    --divider-blue: #223457;
    --rule-grey: #8c96a6;
  }
  * { box-sizing: border-box; margin: 0; padding: 0; }
  html, body {
    width: 1200px;
    height: 900px;
    overflow: hidden;
  }
  body {
    background: var(--backdrop);
    font-family: "Questrial", "Century Gothic", sans-serif;
    color: var(--ink-white);
    position: relative;
  }
  .business-card {
    position: absolute;
    left: 150px;
    top: 190px;
    width: 900px;
    height: 520px;
    border-radius: 4px;
    background:
      repeating-linear-gradient(0deg, rgba(255,255,255,0.025) 0 1px, rgba(0,0,0,0.02) 1px 3px),
      linear-gradient(160deg, var(--card-top), var(--card-bottom));
    box-shadow: 0 18px 40px rgba(0,0,0,0.45);
  }
  .brand-block {
    position: absolute;
    left: 70px;
    top: 120px;
    width: 420px;
  }
  .brand-name {
    display: flex;
    align-items: center;
    gap: 16px;
    font-size: 40px;
    letter-spacing: 1px;
    line-height: 1;
    color: var(--ink-white);
    text-transform: uppercase;
  }
  .brand-square {
    width: 22px;
    height: 22px;
    background: var(--accent-green);
    flex: none;
  }
  .brand-rule {
    margin-top: 18px;
    height: 1px;
    background: var(--rule-grey);
  }
  .brand-url {
    margin-top: 10px;
    font-size: 19px;
    letter-spacing: 7px;
    color: var(--ink-soft);
  }
  .column-divider {
    position: absolute;
    left: 500px;
    top: 240px;
    width: 1px;
    height: 230px;
    background: var(--divider-blue);
  }
  .contact-block {
    position: absolute;
    left: 540px;
    top: 250px;
  }
  .holder-name {
    font-size: 28px;
    color: var(--accent-green);
    margin-left: 60px;
    margin-bottom: 22px;
  }
  .contact-list {
    list-style: none;
    font-size: 17px;
    color: var(--ink-white);
  }
  .contact-list li {
    display: flex;
    align-items: center;
    gap: 14px;
    height: 30px;
  }
  .contact-icon {
    width: 18px;
    height: 18px;
    flex: none;
    fill: var(--ink-white);
  }
</style>
</head>
<body>
  <main class="business-card">
    <section class="brand-block">
      <h1 class="brand-name"><span class="brand-square"></span>Brightwell Ledger</h1>
      <div class="brand-rule"></div>
      <p class="brand-url">brightwelledger.com.au</p>
    </section>

    <div class="column-divider"></div>

    <section class="contact-block">
      <p class="holder-name">Tobias</p>
      <ul class="contact-list">
        <li>
          <svg class="contact-icon" viewBox="0 0 18 18" aria-hidden="true"><rect x="4" y="1" width="10" height="16" rx="1.5"/><rect x="6" y="3" width="6" height="7" fill="#3d4a60"/></svg>
          61 204 718 39
        </li>
        <li>
          <svg class="contact-icon" viewBox="0 0 18 18" aria-hidden="true"><path d="M4 2c1 0 2 3 2 4s-1.5 1.5-1 2.5 3 3.5 4 4 1.5-1 2.5-1 4 1 4 2-1.5 3-3 3C7 16.5 1.5 11 1.5 5 1.5 3.5 3 2 4 2z"/></svg>
          1390 672 4418
        </li>
        <li>
          <svg class="contact-icon" viewBox="0 0 18 18" aria-hidden="true"><path d="M2 6c2-3 12-3 14 0l-2 2-3-1V5H7v2L4 8z"/><rect x="3" y="10" width="12" height="6" rx="1"/></svg>
          1390 672 4419
        </li>
        <li>
          <svg class="contact-icon" viewBox="0 0 18 18" aria-hidden="true"><path d="M2 4h14v10H2z"/><path d="M2 4l7 6 7-6" fill="none" stroke="#3d4a60" stroke-width="1.4"/></svg>
          hello@brightwelledger.com.au
        </li>
        <li>
          <svg class="contact-icon" viewBox="0 0 18 18" aria-hidden="true"><circle cx="9" cy="9" r="7.5"/><path d="M1.5 9h15M9 1.5c-3 3-3 12 0 15M9 1.5c3 3 3 12 0 15" fill="none" stroke="#3d4a60" stroke-width="1.2"/></svg>
          brightwelledger.com.au
        </li>
      </ul>
    </section>
  </main>
</body>
</html>
```